The Brightwell Clinic :

At The Brightwell Clinic our goal is to provide the most skilled and advanced examination and treatment of the upper neck for superior long-term outcomes for those experiencing headache or migraine.

If a spinal disorder is responsible for the headache and migraine condition the disorder will involve one or more of the top three spinal segments. The fundamental and most powerful feature of The Brightwell Clinic is our method of examining the movements of the top three spinal segments.

We would like the design should communicate professionalism and specialisation.
Updates

Don't necessarily have to have the photos provided.Photo was used for promotional material. I dont have a logo as yet what I  would also like designed.

Project Deadline Extended
Reason: Opening has been delayed due to construction issues of building.

Industry/Entity Type

Clinic

Contact Information for Business Card

The Brightwell Clinic
Suite 3, Oakvale Heath Centre
87 Ferncliff Drive, Port Macquarie NSW 2444
Tel : 63 71 2946 www.thebrightwellclinic.com.au

Requirements
Must have
• Mr Carl Pettigrew
Senior Physiotherapist / Senior Accredited Exercise Physiologist
Ba. App. Sc. (Physiotherapy), Ba Sp. Sc. (Exercise Science), Dip. R.M, MAPA, MESSA, MSMA, MACSM.

Appointment area on back of card

```html
<!DOCTYPE html>
<html lang="en">
<head>
<meta charset="utf-8">
<title>The Brightwell Clinic – Business Card</title>
<link rel="stylesheet" href="https://fonts.googleapis.com/css2?family=Arimo:wght@400;700&display=swap">
<style>
  :root {
    --clinic-blue: #1ba8e0;
    --band-blue: #29abe2;
    --accent-green: #7dc242;
    --accent-purple: #6e2a7e;
    --paper: #ffffff;
    --decor-green: #eef6dc;
    --hair-light: #e6d6b8;
    --hair-mid: #c9b28c;
    --hair-dark: #9c8866;
    --skin-light: #f6e9de;
    --skin-mid: #e8cdb8;
    --skin-shadow: #c99e84;
  }
  html, body {
    margin: 0;
    padding: 0;
    width: 1200px;
    height: 741px;
    overflow: hidden;
    background: var(--paper);
  }
  .card {
    position: relative;
    width: 1200px;
    height: 741px;
    background: var(--paper);
    font-family: 'Arimo', Arial, sans-serif;
    overflow: hidden;
  }
  .decor-flourish {
    position: absolute;
    left: 60px;
    top: 10px;
    width: 340px;
    height: 690px;
    border-radius: 50%;
    background: radial-gradient(ellipse at center, var(--decor-green) 0%, rgba(238,246,220,0) 68%);
  }
  .clinic-name {
    position: absolute;
    right: 713px;
    top: 57px;
    margin: 0;
    font-size: 42px;
    font-weight: 400;
    line-height: 48px;
    color: var(--clinic-blue);
    white-space: nowrap;
  }
  .rule {
    position: absolute;
    left: 0;
    width: 500px;
    height: 1.5px;
  }
  .rule--blue { top: 107px; background: var(--clinic-blue); }
  .rule--green { top: 452px; background: var(--accent-green); }
  .address {
    position: absolute;
    right: 716px;
    top: 116px;
    margin: 0;
    font-style: normal;
    text-align: right;
    font-size: 20.5px;
    line-height: 27.5px;
    color: var(--clinic-blue);
  }
  .practitioner {
    position: absolute;
    right: 722px;
    top: 405px;
    margin: 0;
    font-size: 37px;
    font-weight: 400;
    line-height: 42px;
    color: var(--accent-green);
    white-space: nowrap;
  }
  .credentials {
    position: absolute;
    right: 722px;
    top: 470px;
    margin: 0;
    padding: 0;
    list-style: none;
    text-align: right;
    font-size: 18px;
    line-height: 24.3px;
    color: var(--accent-green);
    white-space: nowrap;
  }
  .credentials .sep {
    color: var(--accent-purple);
    font-weight: 700;
    padding: 0 2px;
  }
  .phone {
    position: absolute;
    right: 722px;
    top: 652px;
    display: flex;
    align-items: center;
    gap: 12px;
    font-size: 32px;
    color: var(--accent-purple);
    white-space: nowrap;
  }
  .phone svg { width: 22px; height: 38px; }
  .divider-thin {
    position: absolute;
    top: 0;
    left: 499px;
    width: 3px;
    height: 741px;
    background: var(--band-blue);
  }
  .divider-thin--second { left: 505px; width: 1.5px; }
  .band-blue {
    position: absolute;
    top: 0;
    left: 515px;
    width: 19px;
    height: 741px;
    background: var(--band-blue);
  }
  .band-purple {
    position: absolute;
    top: 0;
    left: 538px;
    width: 40px;
    height: 741px;
    background: var(--accent-purple);
    overflow: hidden;
  }
  .band-purple .web {
    position: absolute;
    left: 9px;
    top: 880px;
    transform: rotate(-90deg);
    transform-origin: left top;
    height: 22px;
    line-height: 22px;
    font-size: 18px;
    font-weight: 700;
    letter-spacing: 0.2px;
    color: var(--paper);
    white-space: nowrap;
  }
  .band-purple .web span { margin-right: 24px; }
  .photo {
    position: absolute;
    top: 0;
    left: 584px;
    width: 616px;
    height: 741px;
    background:
      radial-gradient(ellipse 150px 90px at 360px 150px, rgba(255,255,255,0.55) 0%, rgba(255,255,255,0) 100%),
      radial-gradient(ellipse 260px 320px at 420px 330px, rgba(250,238,228,0.9) 0%, rgba(250,238,228,0) 100%),
      radial-gradient(ellipse 200px 160px at 560px 560px, rgba(201,158,132,0.55) 0%, rgba(201,158,132,0) 100%),
      radial-gradient(ellipse 120px 260px at 160px 520px, rgba(156,136,102,0.45) 0%, rgba(156,136,102,0) 100%),
      linear-gradient(90deg,
        var(--hair-light) 0%,
        var(--hair-mid) 6%,
        var(--hair-light) 11%,
        var(--hair-dark) 16%,
        var(--hair-mid) 21%,
        var(--skin-mid) 30%,
        var(--skin-light) 45%,
        var(--skin-light) 82%,
        var(--skin-mid) 93%,
        var(--skin-shadow) 100%);
  }
</style>
</head>
<body>
  <main class="card">
    <div class="decor-flourish" role="img" aria-label="Faint green script flourish decoration"></div>

    <h1 class="clinic-name">The Brightwell Clinic</h1>
    <div class="rule rule--blue"></div>
    <address class="address">
      Suite 3, Oakvale Heath Centre<br>
      87 Ferncliff Drive<br>
      Port Macquarie NSW 2444
    </address>

    <h2 class="practitioner">Mr Carl Pettigrew</h2>
    <div class="rule rule--green"></div>
    <ul class="credentials">
      <li>Senior Physiotherapist</li>
      <li>Senior Accredited Exercise Physiologist</li>
      <li>Ba. App. Sc. (Physiotherapy)</li>
      <li>Ba Sp. Sc. (Exercise Science)</li>
      <li>Dip. R.M <span class="sep">I</span> MAPA <span class="sep">I</span> MESSA <span class="sep">I</span> MSMA <span class="sep">I</span> MACSM</li>
    </ul>

    <div class="phone">
      <svg viewBox="0 0 22 38" aria-hidden="true">
        <path d="M15 1 L19 2 L17 12 L12 11 C10 15 10 23 12 27 L17 26 L19 36 L15 37 C7 37 2 29 2 19 C2 9 7 1 15 1 Z" fill="currentColor"/>
        <path d="M12 11 C10 15 10 23 12 27" fill="none" stroke="#ffffff" stroke-width="1.2"/>
      </svg>
      <span>63 71 2946</span>
    </div>

    <div class="divider-thin"></div>
    <div class="divider-thin divider-thin--second"></div>
    <div class="band-blue"></div>
    <div class="band-purple">
      <div class="web"><span>www.thebrightwellclinic.com.au</span><span>www.thebrightwellclinic.com.au</span><span>www.thebrightwellclinic.com.au</span><span>www.thebrightwellclinic.com.au</span></div>
    </div>

    <div class="photo" role="img" aria-label="Close-up promotional photograph of a smiling woman with blonde hair"></div>
  </main>
</body>
</html>
```